Tumbril Deli Needs a Web Page!

Tumbril Deli is a gourmet sandwich shop in Baltimore, MD USA.
We are due to open in about a month or so and we need a great web page that looks cool and is easy to use. Our Concept supports local farmers, ranchers, fishmongers & purveyors. All of our menu items are made from scratch using fresh local ingredients.

Target Market(s)

Urban people on the go & Anyone who is hungry and likes a great sandwich

Industry/Entity Type

Shop

Requirements
Must have
• We must have these 8 tabs:
Home
Menus
Gallery
About Us
Media & Events
Hours & Location
Order Online
Contact Us

Also we would like our Logo to be a focal point
Our Color scheme is Red, Black, Grey, White and a reddish-orange
however any and all colors are great and will be considered
We would love an area on the page for our own food photos to be added.
Nice to have
• Baltimore Skyline
Order Online Now Button
Free Wi-Fi Symbol
Dine-In, Take Out, Delivery,
Business Lunches, Tail Gate Platters, Catering
Should not have
• No Stock images of food or chefs.
(We want to put all of our own food photos up later.)
No Pink.

```html
<!DOCTYPE html>
<html lang="en">
<head>
<meta charset="utf-8">
<title>Tumbril Deli</title>
<link rel="stylesheet" href="https://fonts.googleapis.com/css2?family=Arimo:wght@400;700&family=Maven+Pro:wght@500;700&family=Gelasio&family=Oranienbaum&display=swap">
<style>
:root{
  --paper:#f1efeb;
  --paper-line:#e2dfda;
  --slider-bg:#d6d3cf;
  --ink:#1d1d1d;
  --body:#3a3a3a;
  --red:#c9391a;
  --red-dark:#9c2410;
  --orange:#e9641c;
  --footer:#232323;
  --footer-line:#3b3b3b;
  --footer-text:#b9b9b9;
  --field:#2d2d2d;
}
*{box-sizing:border-box;margin:0;padding:0}
html,body{width:805px;height:1200px;overflow:hidden}
body{position:relative;background:var(--paper);font-family:"Arimo",Arial,sans-serif;color:var(--ink)}
.abs{position:absolute}

/* header */
.brand{left:55px;top:10px;width:140px;height:90px;display:flex;align-items:center;gap:8px}
.brand-dot{width:22px;height:22px;border-radius:50%;background:var(--red);flex:none}
.brand-name{font-family:"Maven Pro",sans-serif;font-weight:700;font-size:22px;line-height:1.05;color:var(--ink);text-transform:uppercase}
.skyline{left:254px;top:28px;width:492px;height:63px;border:2px solid #3c3c3c;border-radius:3px;
  background:linear-gradient(180deg,#141a2b 0%,#1d2238 45%,#6a4a2c 62%,#1a2135 70%,#0e1220 100%)}

/* nav */
.nav{left:0;top:113px;width:805px;height:27px;border-top:1px solid var(--paper-line);border-bottom:1px solid var(--paper-line)}
.nav a{position:absolute;top:6px;font-size:10.5px;font-weight:700;color:var(--ink);text-decoration:none}
.nav .current{left:59px;top:3px;width:56px;height:20px;border-radius:5px;background:linear-gradient(#e05426,var(--red-dark));color:#fff;text-align:center;line-height:20px}

/* slider */
.slider{left:0;top:140px;width:805px;height:329px;background:var(--slider-bg)}
.slide{left:90px;top:150px;width:624px;height:291px;box-shadow:0 1px 4px rgba(0,0,0,.35);
  background:linear-gradient(180deg,#c8401b 0%,#e6a72a 18%,#b62c17 36%,#4a130c 62%,#1c0907 100%)}
.arrow{top:270px}
.dots{left:379px;top:450px;display:flex;gap:5px}
.dots span{width:9px;height:9px;border-radius:50%;background:#3a0f0a}
.dots span.on{background:#e13b14}

/* specials */
.section-title{font-family:"Maven Pro",sans-serif;font-weight:500;font-size:12.5px;letter-spacing:.2px;color:var(--ink)}
.specials-title{left:88px;top:490px;width:623px;text-align:center}
.specials-title span{background:var(--paper);padding:0 8px;position:relative}
.specials-title:before{content:"";position:absolute;left:0;right:0;top:8px;border-top:1px solid #cfcbc5}
.dish{top:530px;width:138px}
.dish-photo{position:absolute;left:8px;top:0;width:124px;height:124px;border-radius:50%;border:5px solid #fff;box-shadow:0 0 0 1px #d8d4cf,0 2px 4px rgba(0,0,0,.15)}
.more{position:absolute;left:108px;top:92px;width:34px;height:16px;background:var(--red);color:#fff;font-size:6.5px;font-weight:700;line-height:16px;text-align:center;clip-path:polygon(20% 0,100% 0,100% 100%,20% 100%,0 50%)}
.dish-head{position:absolute;top:138px;left:0;width:148px;display:flex;justify-content:space-between;align-items:baseline}
.dish-name{font-family:"Maven Pro",sans-serif;font-weight:500;font-size:12.5px}
.price{font-family:"Gelasio",serif;font-size:17px;color:var(--red)}
.dish-sub{position:absolute;top:160px;font-size:9px;font-weight:400;color:var(--ink)}
.dish-text{position:absolute;top:177px;width:138px;font-size:7.5px;line-height:9.5px;color:var(--body);text-align:justify}

.divider{left:0;top:763px;width:805px;border-top:1px solid #fff}

/* welcome */
.welcome-title{left:88px;top:779px}
.welcome-photo{left:97px;top:811px;width:70px;height:90px;border:3px solid #fff;box-shadow:0 0 0 1px #d8d4cf;background:linear-gradient(160deg,#8a6a55,#3b2a22 60%,#cfc7bd)}
.welcome-lead{left:178px;top:808px;width:320px;font-size:8.2px;font-weight:700;line-height:10px;color:var(--ink)}
.welcome-text{left:178px;top:836px;width:320px;font-size:7.6px;line-height:9.3px;color:var(--body);text-align:justify}
.btn{height:16px;border-radius:4px;background:linear-gradient(#de5228,var(--red-dark));color:#fff;font-size:6.5px;font-weight:700;line-height:16px;text-align:center;text-transform:uppercase}
.read-more{left:180px;top:914px;width:49px}
.photos-title{left:518px;top:779px}
.thumb{width:42px;height:42px;border:3px solid #fff;box-shadow:0 0 0 1px #d8d4cf}
.view-all{left:651px;top:914px;width:67px}

/* footer */
.footer{left:0;top:952px;width:805px;height:248px;background:var(--footer)}
.foot-title{top:969px;width:143px;padding-bottom:7px;border-bottom:1px solid var(--footer-line);font-family:"Oranienbaum",serif;font-size:17px;color:#e8e8e8;text-transform:uppercase}
.links{top:1011px;list-style:none;font-size:8.5px;color:var(--footer-text)}
.links li{height:22px}
.links li:before{content:"›";margin-right:8px;color:#dcdcdc}
.post{width:145px;height:40px}
.post-thumb{position:absolute;left:0;top:0;width:39px;height:39px;border:2px solid #555}
.post-title{position:absolute;left:48px;top:0;font-size:8.5px;color:#ddd}
.post-text{position:absolute;left:48px;top:13px;font-size:7.3px;line-height:11px;color:var(--footer-text)}
.social{top:1011px;list-style:none;font-size:8px;color:var(--footer-text)}
.social li{height:22px;display:flex;align-items:center;gap:10px}
.social i{width:17px;height:17px;border-radius:50%;background:radial-gradient(circle at 40% 35%,#8fd0f2,#2d7fb4)}
.social i.feed{background:radial-gradient(circle at 40% 35%,#f8b56b,#d9591a)}
.field{left:558px;width:145px;height:19px;background:var(--field);border:1px solid #333;border-radius:2px;font-size:6.5px;color:#999;padding-left:8px;line-height:17px}
.field-area{height:56px}
.submit{left:558px;top:1119px;width:41px;height:19px;background:var(--field);border:1px solid #3a3a3a;color:#aaa;font-size:7px;line-height:17px;text-align:center}
.copyright{left:55px;top:1149px;width:691px;height:37px;border-radius:6px;border:1px solid #f08a2d;background:linear-gradient(#e8791e,#b92f10 70%,#a3250c);color:#fbe4d2;font-size:6.5px;line-height:37px;text-align:center}
</style>
</head>
<body>

<header>
  <div class="abs brand"><span class="brand-dot"></span><span class="brand-name">Tumbril<br>Deli</span></div>
  <div class="abs skyline" role="img" aria-label="Night skyline of the harbour city reflected in the water"></div>
</header>

<nav class="abs nav">
  <a class="current" href="#">Home</a>
  <a href="#" style="left:141px">Menus</a>
  <a href="#" style="left:213px">Gallery</a>
  <a href="#" style="left:285px">About Us</a>
  <a href="#" style="left:365px">Media &amp; Events</a>
  <a href="#" style="left:474px">Hours &amp; Location</a>
  <a href="#" style="left:591px">Order Online</a>
  <a href="#" style="left:688px">Contact Us</a>
</nav>

<section class="abs slider" aria-label="Featured events"></section>
<div class="abs slide" role="img" aria-label="Crowded banquet hall under a red and yellow draped tent ceiling"></div>
<svg class="abs arrow" style="left:58px" width="20" height="36" viewBox="0 0 20 36"><path d="M18 1 L2 18 L18 35" fill="none" stroke="#222" stroke-width="1.3"/></svg>
<svg class="abs arrow" style="left:727px" width="20" height="36" viewBox="0 0 20 36"><path d="M2 1 L18 18 L2 35" fill="none" stroke="#222" stroke-width="1.3"/></svg>
<div class="abs dots"><span class="on"></span><span></span><span></span><span></span></div>

<h2 class="abs section-title specials-title"><span>TONIGHT SPECIALS</span></h2>

<article class="abs dish" style="left:88px">
  <div class="dish-photo" role="img" aria-label="Appetizer plate of tomato and greens" style="background:radial-gradient(circle at 40% 40%,#6fa33a,#c2301c 55%,#f2e8df 80%)"></div>
  <span class="more">MORE</span>
  <div class="dish-head"><span class="dish-name">APPETIZER</span><span class="price">$12.95</span></div>
  <p class="dish-sub">Lorem Ipsum is simply dummy text</p>
  <p class="dish-text">Lorem Ipsum has been the industry's standard dummy text ever since the 1500s, when an unknown printer took a galley of type and scrambled.</p>
</article>
<article class="abs dish" style="left:248px">
  <div class="dish-photo" role="img" aria-label="Grilled steak with fries and sauce" style="background:radial-gradient(circle at 60% 60%,#5a2e1c,#b57a3a 50%,#e8c46a 75%)"></div>
  <span class="more">MORE</span>
  <div class="dish-head"><span class="dish-name">MAIN COURSE</span><span class="price">$24.95</span></div>
  <p class="dish-sub">Lorem Ipsum is simply dummy text</p>
  <p class="dish-text">Lorem Ipsum has been the industry's standard dummy text ever since the 1500s, when an unknown printer took a galley of type and scrambled.</p>
</article>
<article class="abs dish" style="left:409px">
  <div class="dish-photo" role="img" aria-label="Dessert with red berries and cream" style="background:radial-gradient(circle at 50% 50%,#c8202a,#e9b7a3 55%,#f4ece6 80%)"></div>
  <span class="more">MORE</span>
  <div class="dish-head"><span class="dish-name">DESSERT</span><span class="price">$14.95</span></div>
  <p class="dish-sub">Lorem Ipsum is simply dummy text</p>
  <p class="dish-text">Lorem Ipsum has been the industry's standard dummy text ever since the 1500s, when an unknown printer took a galley of type and scrambled.</p>
</article>
<article class="abs dish" style="left:569px">
  <div class="dish-photo" role="img" aria-label="Cup of coffee with latte art" style="background:radial-gradient(circle at 45% 50%,#a8765a,#e9e4df 50%,#cfcac4 85%)"></div>
  <span class="more">MORE</span>
  <div class="dish-head"><span class="dish-name">COFFEE</span><span class="price">$5.95</span></div>
  <p class="dish-sub">Lorem Ipsum is simply dummy text</p>
  <p class="dish-text">Lorem Ipsum has been the industry's standard dummy text ever since the 1500s, when an unknown printer took a galley of type and scrambled.</p>
</article>

<div class="abs divider"></div>

<h2 class="abs section-title welcome-title">WELCOME</h2>
<div class="abs welcome-photo" role="img" aria-label="Guest holding a glass of red wine"></div>
<p class="abs welcome-lead">Lorem Ipsum has been the industry's standard dummy text ever since the 1500s, when an unknown printer took a galley of type and scrambled.</p>
<p class="abs welcome-text">Lorem Ipsum has been the industry's standard dummy text ever since the 1500s, when an unknown printer took a galley of type and scrambled. Lorem Ipsum has been the industry's standard dummy text ever since the 1500s, when an unknown printer took a galley of type and scrambled. Lorem Ipsum has been the industry's standard dummy text ever since the 1500s, when an unknown printer took a galley of type and scrambled.Lorem Ipsum has been the industry's standard dummy text ever since the 1500s, when an unknown printer took a galley of type and scrambled.</p>
<a class="abs btn read-more">Read more</a>

<h2 class="abs section-title photos-title">LATEST PHOTOS</h2>
<div class="abs thumb" style="left:525px;top:811px;background:linear-gradient(#8a4a2c,#e9e1d9)" role="img" aria-label="Steak thumbnail"></div>
<div class="abs thumb" style="left:576px;top:811px;background:linear-gradient(#5f9a3a,#c8331d)" role="img" aria-label="Salad thumbnail"></div>
<div class="abs thumb" style="left:627px;top:811px;background:linear-gradient(#e9dcd2,#c32a2c)" role="img" aria-label="Dessert thumbnail"></div>
<div class="abs thumb" style="left:678px;top:811px;background:linear-gradient(#6f9f3e,#cf4a24)" role="img" aria-label="Appetizer thumbnail"></div>
<div class="abs thumb" style="left:525px;top:862px;background:linear-gradient(#d48b2a,#f1e8de)" role="img" aria-label="Plated dish thumbnail"></div>
<div class="abs thumb" style="left:576px;top:862px;background:linear-gradient(#9b6a4e,#ece7e2)" role="img" aria-label="Coffee thumbnail"></div>
<div class="abs thumb" style="left:627px;top:862px;background:linear-gradient(#b5262c,#e7cfc4)" role="img" aria-label="Berry dessert thumbnail"></div>
<div class="abs thumb" style="left:678px;top:862px;background:linear-gradient(#5e9a37,#8a4a2c)" role="img" aria-label="Grill plate thumbnail"></div>
<a class="abs btn view-all">View all photos</a>

<footer>
  <div class="abs footer"></div>
  <h3 class="abs foot-title" style="left:60px">Useful Resources</h3>
  <ul class="abs links" style="left:60px">
    <li>Lorem ipsum Dolor Sit Amet</li>
    <li>Lorem ipsum Dolor Sit Amet</li>
    <li>Lorem ipsum Dolor Sit Amet</li>
    <li>Lorem ipsum Dolor Sit Amet</li>
    <li>Lorem ipsum Dolor Sit Amet</li>
  </ul>

  <h3 class="abs foot-title" style="left:228px">Blog Posts</h3>
  <div class="abs post" style="left:228px;top:1012px">
    <div class="post-thumb" role="img" aria-label="Sunset over dunes" style="background:linear-gradient(#e9a23b,#c25a1e)"></div>
    <span class="post-title">Lorem Ipsum is simply</span>
    <span class="post-text">The printing and typesetting<br>industry has been industry...</span>
  </div>
  <div class="abs post" style="left:228px;top:1064px">
    <div class="post-thumb" role="img" aria-label="Ball on a green field" style="background:linear-gradient(#4a86c8,#3e8a2e)"></div>
    <span class="post-title">Lorem Ipsum is simply</span>
    <span class="post-text">The printing and typesetting<br>industry has been industry...</span>
  </div>

  <h3 class="abs foot-title" style="left:394px">Get Social</h3>
  <ul class="abs social" style="left:394px">
    <li><i></i>Follow us on Chirper</li>
    <li><i></i>Friendship on Friendbook</li>
    <li><i></i>Visit us on WorkLink</li>
    <li><i></i>See our Vids on ViewReel</li>
    <li><i class="feed"></i>Subscribe to RSS Feed</li>
  </ul>

  <h3 class="abs foot-title" style="left:558px">Contact Us</h3>
  <div class="abs field" style="top:1011px">Name</div>
  <div class="abs field" style="top:1034px">Email</div>
  <div class="abs field field-area" style="top:1057px"></div>
  <div class="abs submit">Submit</div>

  <div class="abs copyright">© COPYRIGHTS 2012. ALL RIGHTS RESERVED.</div>
</footer>

</body>
</html>
```